Software company needs a web design

We need a web design for the main page of our company, called Brixel Software (where Brixel goes for Brisk Pixel Firm). We develop and sell software for SME as well as Corporate sector within whole European continent.
Our main products are now OVN 7, an (real estate) asset management software enabling efficient management of commercial real estates; DUNE, software for loan management and two HR applications.
As our philosophy is efficiency, focusing on substance, getting rid of cumulated ballast etc., we'd like the web showing the same, i.e. being simple intuitive, rather visual then having too much text but still presenting our products (and our company via them) properly.
People visiting the web should easily find the right information on the company, people behind and our products as well as getting the right impression on what we aim to.
Attached is our company logo.

```html
<!DOCTYPE html>
<html lang="en">
<head>
<meta charset="utf-8">
<title>Brixel Software</title>
<link href="https://fonts.googleapis.com/css2?family=Lato:wght@300;400;700;900&family=Open+Sans:ital,wght@0,400;0,600;0,700;1,400&display=swap" rel="stylesheet">
<style>
:root{
  --navy:#1d2440;
  --ink:#2b2b2b;
  --muted:#6b6f7a;
  --accent:#1479b9;
  --accent-dark:#0f5f93;
  --band:#ececf5;
  --blue:#1c87c9;
  --white:#ffffff;
  --line:#e2e4ea;
  --star:#f5c518;
  --tint:#e6f1fa;
}
*{box-sizing:border-box;margin:0;padding:0}
html,body{width:1200px;height:3462px;overflow:hidden;background:var(--white)}
body{font-family:"Open Sans",Arial,sans-serif;color:var(--ink);position:relative}
.abs{position:absolute}
h1,h2,h3{font-family:"Lato",Arial,sans-serif;font-weight:400}

/* header */
.site-header{position:absolute;left:0;top:0;width:1200px;height:111px;background:var(--white)}
.brand{position:absolute;left:112px;top:26px;display:flex;align-items:center;gap:14px}
.brand-mark{width:22px;height:22px;background:var(--navy)}
.brand-name{font-family:"Lato",sans-serif;font-weight:700;font-size:40px;color:var(--navy);letter-spacing:.5px}
.quick-contact{position:absolute;right:110px;top:24px;font-size:17px;font-weight:600;color:var(--navy);display:flex;align-items:center;gap:8px}
.main-nav{position:absolute;right:110px;top:72px;display:flex;gap:34px;font-size:16px;font-weight:600;color:var(--navy);align-items:center}
.main-nav .active{color:var(--accent)}

/* hero */
.hero{position:absolute;left:0;top:111px;width:1200px;height:597px;overflow:hidden;
  background:linear-gradient(180deg,#8ea3b8 0%,#b9b4a8 45%,#8b7a62 65%,#5f6a6e 100%)}
.hero-shade{position:absolute;inset:0;background:rgba(20,30,45,.32)}
.hero-title{position:absolute;left:0;width:1200px;top:112px;text-align:center;color:var(--white);font-family:"Lato",sans-serif;font-size:92px;line-height:1.1}
.hero-title b{font-weight:900}
.hero-title span{font-weight:300}
.hero-sub{position:absolute;left:0;width:1200px;top:238px;text-align:center;color:var(--white);font-size:25px;font-weight:600;line-height:39px}
.hero-btn{position:absolute;left:502px;top:350px;width:196px;height:60px;border:2px solid var(--white);color:var(--white);font-size:16px;font-weight:700;display:flex;align-items:center;justify-content:center;letter-spacing:.5px}
.hero-dots{position:absolute;left:564px;top:516px;display:flex;gap:6px}
.hero-dots i{width:14px;height:14px;border-radius:50%;border:2px solid var(--white);display:block}
.hero-dots i.on{background:var(--white)}
.sq{position:absolute;background:var(--white)}

/* welcome */
.welcome{position:absolute;left:0;top:708px;width:1200px;height:574px;overflow:hidden}
.tint{position:absolute;background:var(--tint);opacity:.7}
.welcome h2{position:absolute;left:110px;top:110px;font-size:46px;line-height:56px;color:var(--navy)}
.welcome h2 b{font-weight:900}
.welcome h2 span{font-weight:300}
.welcome p{position:absolute;left:110px;top:235px;width:450px;font-size:14.5px;line-height:31px;color:#555}
.btn{position:absolute;background:var(--accent);color:var(--white);font-size:15px;font-weight:700;display:flex;align-items:center;justify-content:center;letter-spacing:.3px}
.video-frame{position:absolute;left:612px;top:132px;width:476px;height:324px;border:4px solid var(--navy);padding:10px;background:var(--white)}
.video-media{width:100%;height:100%;background:linear-gradient(135deg,#c9d3dc 0%,#9aa9b6 45%,#3c4a58 100%);position:relative}
.play{position:absolute;left:50%;top:50%;width:74px;height:74px;margin:-37px 0 0 -37px;border-radius:50%;background:#1a1a1a}
.play:after{content:"";position:absolute;left:29px;top:22px;border-left:24px solid var(--white);border-top:15px solid transparent;border-bottom:15px solid transparent}

/* products */
.products{position:absolute;left:0;top:1282px;width:1200px;height:655px;background:var(--band);overflow:hidden}
.section-title{position:absolute;left:0;width:1200px;text-align:center;font-size:44px;color:var(--navy)}
.section-title b{font-weight:900}
.section-title span{font-weight:300}
.product{position:absolute;top:176px;width:233px;text-align:center}
.product-media{width:233px;height:229px;border:5px solid var(--white);box-shadow:0 0 0 1px #d6d8e2}
.product h3{margin-top:30px;font-size:23px;font-weight:700;color:var(--navy)}
.product p{margin:14px auto 0;width:210px;font-size:14px;line-height:24px;color:var(--muted)}

/* blog */
.blog{position:absolute;left:0;top:1937px;width:1200px;height:736px}
.post{position:absolute;top:188px;width:311px;height:448px}
.post-media{position:absolute;left:0;top:0;width:311px;height:240px}
.post-body{position:absolute;left:13px;top:217px;width:285px;height:231px;background:var(--white);box-shadow:0 2px 8px rgba(0,0,0,.16);padding:20px 22px}
.post-body h3{font-size:21px;font-weight:700;color:var(--navy)}
.post-meta{margin-top:12px;font-size:13px;color:#444;display:flex;align-items:center;gap:6px}
.post-body p{margin-top:12px;font-size:13px;line-height:23px;color:#555}
.read-more{display:block;margin-top:14px;font-size:13px;font-weight:700;color:var(--accent)}

/* testimonials */
.testimonials{position:absolute;left:0;top:2673px;width:1200px;height:447px;background:var(--blue);overflow:hidden}
.testimonials .section-title{color:var(--white)}
.quote{position:absolute;top:186px;width:330px}
.avatar{position:absolute;left:0;top:0;width:74px;height:74px;border-radius:50%;border:3px solid var(--white)}
.quote blockquote{position:absolute;left:90px;top:0;width:232px;color:#e6f2fb;font-style:italic;font-size:13px;line-height:22px}
.quote blockquote b{font-style:normal;font-size:22px;color:var(--white);margin-right:6px;font-weight:700}
.quote cite{position:absolute;left:90px;top:124px;font-style:normal;font-weight:700;font-size:13px;color:var(--white);letter-spacing:.4px;white-space:nowrap}
.stars{position:absolute;left:90px;top:148px;display:flex;gap:4px}
.arrow{position:absolute;top:242px;width:36px;height:36px;border-radius:50%;border:2px solid rgba(255,255,255,.8)}

/* footer */
.site-footer{position:absolute;left:0;top:3120px;width:1200px;height:342px;text-align:center}
.social{position:absolute;left:483px;top:104px;display:flex;gap:9px}
.social i{display:block;width:51px;height:51px;border-radius:50%;border:1.5px solid #9aa0ae}
.contact-line{position:absolute;left:0;width:1200px;top:192px;font-size:15px;color:#444;display:flex;justify-content:center;align-items:center;gap:10px}
.contact-line .sep{color:#888}
.footer-links{position:absolute;left:0;width:1200px;top:230px;font-size:15px;color:#444;display:flex;justify-content:center;gap:18px}
.copyright{position:absolute;left:0;width:1200px;top:268px;font-size:15px;color:#555}
</style>
</head>
<body>

<header class="site-header">
  <div class="brand"><i class="brand-mark"></i><span class="brand-name">Brixel Software</span></div>
  <div class="quick-contact">
    <svg width="16" height="16" viewBox="0 0 24 24"><path fill="#1479b9" d="M6.6 10.8a15 15 0 0 0 6.6 6.6l2.2-2.2c.3-.3.7-.4 1-.2 1.1.4 2.3.6 3.6.6.6 0 1 .4 1 1V20c0 .6-.4 1-1 1A17 17 0 0 1 3 4c0-.6.4-1 1-1h3.5c.6 0 1 .4 1 1 0 1.3.2 2.5.6 3.6.1.3 0 .7-.2 1z"/></svg>
    Quick Contact: Kestrelova 48/12, Old Town, 110 00 Praha 1
  </div>
  <nav class="main-nav">
    <span class="active">Home</span><span>About us</span><span>Services</span><span>Products</span><span>Blog</span><span>Contact Us</span>
    <svg width="16" height="16" viewBox="0 0 24 24"><circle cx="10" cy="10" r="6.5" fill="none" stroke="#1d2440" stroke-width="3"/><path d="M15 15l6 6" stroke="#1d2440" stroke-width="3"/></svg>
  </nav>
</header>

<section class="hero">
  <div role="img" aria-label="City riverside with historic stone bridge and old town buildings" class="abs" style="inset:0"></div>
  <div class="hero-shade"></div>
  <i class="sq" style="left:0;top:0;width:70px;height:66px;opacity:.85"></i>
  <i class="sq" style="left:84px;top:94px;width:46px;height:46px"></i>
  <i class="sq" style="left:32px;top:158px;width:28px;height:28px"></i>
  <i class="sq" style="left:1070px;top:414px;width:72px;height:70px;opacity:.9"></i>
  <i class="sq" style="left:1156px;top:508px;width:44px;height:48px"></i>
  <i class="sq" style="left:1104px;top:570px;width:30px;height:27px"></i>
  <h1 class="hero-title"><b>Brixel</b> <span>Software</span></h1>
  <p class="hero-sub">We develop and sell software for SME as well as Corporate<br>sector within whole European continent</p>
  <div class="hero-btn">GET MORE INFO</div>
  <div class="hero-dots"><i class="on"></i><i></i><i></i><i></i></div>
</section>

<section class="welcome">
  <i class="tint" style="left:0;top:0;width:228px;height:220px"></i>
  <i class="tint" style="left:264px;top:200px;width:150px;height:150px"></i>
  <i class="tint" style="left:102px;top:480px;width:100px;height:94px"></i>
  <i class="abs" style="left:1064px;top:64px;width:32px;height:30px;background:var(--accent)"></i>
  <i class="abs" style="left:1104px;top:104px;width:18px;height:18px;background:var(--accent)"></i>
  <i class="abs" style="left:1078px;top:126px;width:10px;height:10px;background:var(--accent)"></i>
  <h2><b>Welcome to</b><br><span>Brixel Software</span></h2>
  <p>Nam libero tempore, cum soluta nobis est eligendi optio cumque nihil impedit quo minus id quod maxime placeat facere possimus, omnisvo luptas assumenda est, omnis dolor repellendus. Temporibus autequi busdam et aut officiis debitis aut rerum necessitatibus saepe evenietr ut et voluptates repudianda ut aut reicien.</p>
  <div class="btn" style="left:110px;top:420px;width:135px;height:47px">READ MORE</div>
  <div class="video-frame">
    <div class="video-media" role="img" aria-label="Laptop showing a software dashboard on an office desk"><span class="play"></span></div>
  </div>
</section>

<section class="products">
  <i class="tint" style="left:820px;top:0;width:224px;height:138px;background:#dfe0ee"></i>
  <i class="tint" style="left:1090px;top:205px;width:110px;height:140px;background:#dfe0ee"></i>
  <h2 class="section-title" style="top:72px"><b>Our</b> <span>Products</span></h2>
  <div class="product" style="left:110px">
    <div class="product-media" role="img" aria-label="Person pointing at charts on a computer screen" style="background:linear-gradient(135deg,#e8edf2,#9fb1c4)"></div>
    <h3>OVN 7</h3>
    <p>(real estate) asset management software enabling efficient management of commercial real estates</p>
  </div>
  <div class="product" style="left:361px">
    <div class="product-media" role="img" aria-label="Couple reviewing documents with an advisor" style="background:linear-gradient(135deg,#5d6470,#c9b9a4)"></div>
    <h3>DUNE</h3>
    <p>Software for loan management</p>
  </div>
  <div class="product" style="left:609px">
    <div class="product-media" role="img" aria-label="Smartphone and laptop with network graphics" style="background:linear-gradient(135deg,#2b5fd0,#8fb6ef)"></div>
    <h3>HR applications 1</h3>
    <p>At vero eos et accusaus et iusto odio dignissimos ducim</p>
  </div>
  <div class="product" style="left:857px">
    <div class="product-media" role="img" aria-label="Hand holding a phone in front of analytics screens" style="background:linear-gradient(135deg,#cfe0ef,#3f7dc0)"></div>
    <h3>HR applications 2</h3>
    <p>At vero eos et accusaus et iusto odio dignissimos ducim</p>
  </div>
</section>

<section class="blog">
  <h2 class="section-title" style="top:80px"><b>Latest</b> <span>Blog</span></h2>
  <article class="post" style="left:110px">
    <div class="post-media" role="img" aria-label="Hands holding a tablet with charts" style="background:linear-gradient(135deg,#dfe6ec,#7e93a8)"></div>
    <div class="post-body">
      <h3>Finibus Bonoruet Mal</h3>
      <div class="post-meta"><svg width="12" height="12" viewBox="0 0 12 12"><rect x="1" y="2" width="10" height="9" fill="none" stroke="#1479b9" stroke-width="1.5"/><path d="M1 5h10" stroke="#1479b9" stroke-width="1.5"/></svg>18/06/2018 &nbsp;|&nbsp; <svg width="12" height="12" viewBox="0 0 12 12"><circle cx="6" cy="4" r="2.5" fill="#1479b9"/><path d="M1.5 11.5a4.5 4.5 0 0 1 9 0z" fill="#1479b9"/></svg>Ian Holt</div>
      <p>Nam libero tempore, cum solua nobis est eligendi optio cumque nihilp edit quo minus id quod maxi.</p>
      <span class="read-more">READ MORE</span>
    </div>
  </article>
  <article class="post" style="left:444px">
    <div class="post-media" role="img" aria-label="Pen pointing at a bar chart on paper" style="background:linear-gradient(135deg,#f1f4f8,#5d86d4)"></div>
    <div class="post-body">
      <h3>Finibus Bonoruet Mal</h3>
      <div class="post-meta"><svg width="12" height="12" viewBox="0 0 12 12"><rect x="1" y="2" width="10" height="9" fill="none" stroke="#1479b9" stroke-width="1.5"/><path d="M1 5h10" stroke="#1479b9" stroke-width="1.5"/></svg>18/06/2018 &nbsp;|&nbsp; <svg width="12" height="12" viewBox="0 0 12 12"><circle cx="6" cy="4" r="2.5" fill="#1479b9"/><path d="M1.5 11.5a4.5 4.5 0 0 1 9 0z" fill="#1479b9"/></svg>Ian Holt</div>
      <p>Nam libero tempore, cum solua nobis est eligendi optio cumque nihilp edit quo minus id quod maxi.</p>
      <span class="read-more">READ MORE</span>
    </div>
  </article>
  <article class="post" style="left:778px">
    <div class="post-media" role="img" aria-label="Hands using a tablet with a dashboard" style="background:linear-gradient(135deg,#3a4350,#9fb4c8)"></div>
    <div class="post-body">
      <h3>Finibus Bonoruet Mal</h3>
      <div class="post-meta"><svg width="12" height="12" viewBox="0 0 12 12"><rect x="1" y="2" width="10" height="9" fill="none" stroke="#1479b9" stroke-width="1.5"/><path d="M1 5h10" stroke="#1479b9" stroke-width="1.5"/></svg>18/06/2018 &nbsp;|&nbsp; <svg width="12" height="12" viewBox="0 0 12 12"><circle cx="6" cy="4" r="2.5" fill="#1479b9"/><path d="M1.5 11.5a4.5 4.5 0 0 1 9 0z" fill="#1479b9"/></svg>Ian Holt</div>
      <p>Nam libero tempore, cum solua nobis est eligendi optio cumque nihilp edit quo minus id quod maxi.</p>
      <span class="read-more">READ MORE</span>
    </div>
  </article>
</section>

<section class="testimonials">
  <h2 class="section-title" style="top:76px"><b>Client</b> <span>Testimonials</span></h2>
  <span class="arrow" style="left:28px"><svg width="32" height="32" viewBox="0 0 32 32"><path d="M19 10l-6 6 6 6" fill="none" stroke="#fff" stroke-width="2"/></svg></span>
  <span class="arrow" style="left:1134px"><svg width="32" height="32" viewBox="0 0 32 32"><path d="M13 10l6 6-6 6" fill="none" stroke="#fff" stroke-width="2"/></svg></span>

  <div class="quote" style="left:110px">
    <div class="avatar" role="img" aria-label="Client portrait" style="background:#e2b99a"></div>
    <blockquote><b>“</b>Nam libero tempore, cum solutano bis est eligendi optio cumque nihil impe dit quo minus id quod maxime placeat facere possimus, omnis</blockquote>
    <cite>LEO MARANO</cite>
    <div class="stars">
      <svg width="92" height="16" viewBox="0 0 92 16"><g fill="#f5c518"><path id="s" d="M8 0l2.4 5 5.4.6-4 3.7 1.1 5.4L8 12l-4.9 2.7 1.1-5.4-4-3.7 5.4-.6z"/><use href="#s" x="19"/><use href="#s" x="38"/><use href="#s" x="57"/></g><use href="#s" x="76" fill="none" stroke="#f5c518"/></svg>
    </div>
  </div>
  <div class="quote" style="left:445px">
    <div class="avatar" role="img" aria-label="Client portrait" style="background:#8a7868"></div>
    <blockquote><b>“</b>Nam libero tempore, cum solutano bis est eligendi optio cumque nihil impe dit quo minus id quod maxime placeat facere possimus, omnis</blockquote>
    <cite>RAY DALE FENWICK</cite>
    <div class="stars">
      <svg width="92" height="16" viewBox="0 0 92 16"><g fill="#f5c518"><use href="#s"/><use href="#s" x="19"/><use href="#s" x="38"/><use href="#s" x="57"/></g><use href="#s" x="76" fill="none" stroke="#f5c518"/><path d="M84 0l-2.4 5-5.4.6 4 3.7-1.1 5.4L84 12z" fill="#f5c518"/></svg>
    </div>
  </div>
  <div class="quote" style="left:780px">
    <div class="avatar" role="img" aria-label="Client portrait" style="background:#6b4a3a"></div>
    <blockquote><b>“</b>Nam libero tempore, cum solutano bis est eligendi optio cumque nihil impe dit quo minus id quod maxime placeat facere possimus, omnis</blockquote>
    <cite>MINA SORRELL</cite>
    <div class="stars">
      <svg width="92" height="16" viewBox="0 0 92 16"><g fill="#f5c518"><use href="#s"/><use href="#s" x="19"/><use href="#s" x="38"/><use href="#s" x="57"/></g><use href="#s" x="76" fill="none" stroke="#f5c518"/></svg>
    </div>
  </div>
</section>

<footer class="site-footer">
  <div class="social"><i></i><i></i><i></i><i></i></div>
  <div class="contact-line">
    <svg width="12" height="16" viewBox="0 0 12 16"><path d="M6 0a6 6 0 0 0-6 6c0 4.5 6 10 6 10s6-5.5 6-10a6 6 0 0 0-6-6zm0 8.5A2.5 2.5 0 1 1 6 3.5a2.5 2.5 0 0 1 0 5z" fill="#1479b9"/></svg>
    <span>Kestrelova 48/12, Old Town, 110 00 Praha 1</span><span class="sep">|</span>
    <svg width="14" height="14" viewBox="0 0 24 24"><path fill="#1479b9" d="M6.6 10.8a15 15 0 0 0 6.6 6.6l2.2-2.2c.3-.3.7-.4 1-.2 1.1.4 2.3.6 3.6.6.6 0 1 .4 1 1V20c0 .6-.4 1-1 1A17 17 0 0 1 3 4c0-.6.4-1 1-1h3.5c.6 0 1 .4 1 1 0 1.3.2 2.5.6 3.6.1.3 0 .7-.2 1z"/></svg>
    <span>1 555 010 2040</span><span class="sep">|</span>
    <svg width="16" height="12" viewBox="0 0 16 12"><rect width="16" height="12" rx="1" fill="#1479b9"/><path d="M1 1l7 5 7-5" fill="none" stroke="#fff" stroke-width="1.4"/></svg>
    <span>info@brixelsoftware.cz</span>
  </div>
  <div class="footer-links"><span>Help</span><span>|</span><span>FAQ</span><span>|</span><span>Support</span><span>|</span><span>Sitemap</span><span>|</span><span>Terms Of Use</span><span>|</span><span>Privacy Statement</span></div>
  <div class="copyright">Brixel Software © 2019 All rights reserved.</div>
</footer>

</body>
</html>
```